Meridian Dash add on sales tool2017

This will be a flyer to leave with our clients we just did work for. We want to entice them to use our other services over the next 30 days with a discount, money off etc. we will write in the special and the expiration date. I want the client to read the description and see a picture of the service they may want done.

Target Market(s)

Repeat clients

Industry/Entity Type

Cleaning Service

Font styles to use
Serif
Sans Serif

Colors
ec1f27
000000
b1b1b1

Requirements
Must have
• Call to action! look high end market, clients show we do 1st class work.
• Don't Waite
Nice to have
• Classy, quality, I'm open to using other pictures that may look better
Should not have
• Look like a typical carpet cleaners special flyer
• Not to look cluttered

```html
<!DOCTYPE html>
<html lang="en">
<head>
<meta charset="utf-8">
<title>Meridian Dash – Home Cleaning Services</title>
<link href="https://fonts.googleapis.com/css2?family=Arimo:wght@400;700&family=Roboto:wght@300;700&display=swap" rel="stylesheet">
<style>
  :root {
    --red: #d7262e;
    --black: #231f20;
    --ink: #1d1d1d;
    --panel: #e6e7e8;
    --grey: #b1b1b1;
    --white: #ffffff;
  }
  * { margin: 0; padding: 0; box-sizing: border-box; }
  html, body { width: 927px; height: 1200px; overflow: hidden; background: var(--white); }
  body { font-family: "Arimo", Arial, sans-serif; color: var(--ink); }
  .flyer { position: relative; width: 927px; height: 1200px; border: 2px solid #000; overflow: hidden; }

  .photo { position: absolute; }
  .photo-label { position: absolute; bottom: 10px; color: #fff; font-size: 13px; }

  .service-panel { position: absolute; background: var(--panel); padding: 0 26px; }
  .service-title { font-size: 14.5px; font-weight: 700; line-height: 18px; text-transform: uppercase; }
  .service-text { font-size: 13.4px; line-height: 16.3px; }

  .brand-block {
    position: absolute; left: 617px; top: 46px; width: 265px; height: 187px;
    background: radial-gradient(ellipse at center, #2a2a2a, #0b0b0b);
    display: flex; align-items: center; justify-content: center;
  }
  .brand-name { color: var(--red); font-size: 17px; font-weight: 700; letter-spacing: 1px; text-transform: uppercase; }

  .address { position: absolute; left: 617px; top: 244px; width: 265px; text-align: center; font-size: 13px; }
  .offer-title { position: absolute; left: 617px; top: 281px; width: 265px; text-align: center; color: var(--red); font-size: 17.5px; font-weight: 700; }
  .offer-box { position: absolute; left: 617px; top: 305px; width: 265px; height: 124px; border: 1.5px solid #000; }
  .call-label { position: absolute; left: 617px; top: 436px; width: 265px; text-align: center; font-size: 15px; letter-spacing: 1.5px; }
  .call-phone { position: absolute; left: 617px; top: 450px; width: 265px; text-align: center; font-size: 29px; color: var(--red); }

  .headline-band { position: absolute; left: 0; top: 498px; width: 595px; height: 305px; background: var(--black); padding: 14px 0 0 44px; }
  .headline { font-family: "Roboto", Arial, sans-serif; font-size: 61px; line-height: 56px; text-transform: uppercase; letter-spacing: -1px; }
  .headline .strong { color: var(--red); font-weight: 700; }
  .headline .light { color: var(--grey); font-weight: 300; }
</style>
</head>
<body>
<main class="flyer">

  <div class="photo" style="left:46px;top:46px;width:264px;height:254px;background:linear-gradient(180deg,#6b5a4c,#2d2723 55%,#8f8378);" role="img" aria-label="Technician cleaning draperies in a home with a portable machine"></div>
  <section class="service-panel" style="left:46px;top:300px;width:264px;height:176px;padding-top:24px;">
    <h2 class="service-title">Drapery Cleaning</h2>
    <p class="service-text">Drapery’s act like a filter atracting atmisphiric soil! Making them look dingy, We make it easy to Dry clean in-home! Safe and efective beautiful drapery again.</p>
  </section>

  <div class="photo" style="left:331px;top:46px;width:126px;height:254px;background:linear-gradient(180deg,#d9d6cf,#8d8271 60%,#6b4a3e);" role="img" aria-label="Striped upholstered sofa before cleaning">
    <span class="photo-label" style="left:10px;">Before</span>
  </div>
  <div class="photo" style="left:467px;top:46px;width:128px;height:254px;background:linear-gradient(180deg,#f1efe9,#d9d3c6 60%,#7a4a3e);" role="img" aria-label="Striped upholstered sofa after cleaning">
    <span class="photo-label" style="left:12px;">After</span>
  </div>
  <section class="service-panel" style="left:331px;top:300px;width:264px;height:176px;padding-top:21px;">
    <h2 class="service-title">Upholstery Cleaning</h2>
    <p class="service-text">Every day use leaves your sofa’s and chairs lookng dingy and can smell like dog. Our Dry cleaning ,Shampoo or Rinse extraxtion will leave the fabric feel like clean sheet!</p>
  </section>

  <div class="brand-block"><span class="brand-name">Meridian Dash</span></div>
  <p class="address">4127 W. Canyon Rd. Suite C, Las Vegas</p>
  <h3 class="offer-title">30 DAY SPECIAL OFFER!</h3>
  <div class="offer-box"></div>
  <p class="call-label">CALL NOW TO BOOK</p>
  <p class="call-phone">702 555-0147</p>

  <section class="headline-band">
    <h1 class="headline">
      <span class="strong">One Stop</span><br>
      <span class="light">For All</span><br>
      <span class="light">Your</span> <span class="strong">Home</span><br>
      <span class="strong">Cleaning</span><br>
      <span class="strong">Needs</span>
    </h1>
  </section>

  <div class="photo" style="left:617px;top:498px;width:265px;height:493px;background:linear-gradient(180deg,#f2f2f0,#a57e5e 12%,#c9c4bb 40%,#e7e4dd);" role="img" aria-label="Freshly cleaned carpeted staircase with hardwood landing"></div>
  <section class="service-panel" style="left:617px;top:991px;width:265px;height:163px;padding-top:26px;">
    <h2 class="service-title">Carpet Cleaning</h2>
    <p class="service-text">Don’t let dirty carpets spoil the look of your beautiful home! With 37 years of cleaning carpets experience you can expect your carpets to look like new in most cases.</p>
  </section>

  <div class="photo" style="left:46px;top:827px;width:132px;height:164px;background:linear-gradient(160deg,#a9a39a,#6f6a63);" role="img" aria-label="Stained tile and grout before cleaning">
    <span class="photo-label" style="left:15px;">Before</span>
  </div>
  <div class="photo" style="left:178px;top:827px;width:132px;height:164px;background:linear-gradient(160deg,#cdc6b8,#b6ad9d);" role="img" aria-label="Tile and grout after cleaning">
    <span class="photo-label" style="left:15px;">After</span>
  </div>
  <section class="service-panel" style="left:46px;top:991px;width:264px;height:163px;padding-top:26px;">
    <h2 class="service-title">Tile &amp; Grout Cleaning</h2>
    <p class="service-text">Tile &amp; Grout get neglected! Dirty grout can leave permanent staining. Let our professionals bring back the look of a new floor.</p>
  </section>

  <div class="photo" style="left:331px;top:827px;width:264px;height:164px;background:linear-gradient(180deg,#e9ebea,#9a9c9b 45%,#5e6061);" role="img" aria-label="Polished marble floor in a bright room"></div>
  <section class="service-panel" style="left:331px;top:991px;width:264px;height:163px;padding-top:26px;">
    <h2 class="service-title">Natural Stone<br>Cleaning &amp; Polishing</h2>
    <p class="service-text">A dull stained Marble - Granite-Travertine and other Natural stone can be revitalized to look NEW again!</p>
  </section>

</main>
</body>
</html>
```